Brightway Haul & Repair Services, are a company that offers a 'one stop shop' pre-move clean up a

I have already selected a logo which I would like on the front of the business cards along with phone numbers, web address and email which are:
0419574302
www.brightwayhaul.com.au
brightwayhaulrepair@mailbox.example

On the back of the card I would like to list some of the types of service we offer (clean - move - repairs/maintenance) which are:
CLEAN - windows, gutters, solar panels, driveways/paths, carpets.
MOVE - Small/medium size house/office moves, large item pick-up & delivery, yard clean-up and removal.
General maintenance and repairs.

I would like the blue logo on a gray background.

Thanks

```html
<!DOCTYPE html>
<html lang="en">
<head>
<meta charset="utf-8">
<title>Brightway Haul &amp; Repair Services — Business Cards</title>
<link rel="stylesheet" href="https://fonts.googleapis.com/css2?family=Arimo:wght@400;700&display=swap">
<style>
  :root {
    --brand-blue: #2f78c4;
    --brand-blue-dark: #1f62ad;
    --brand-blue-light: #5e9ad8;
    --card-white: #ffffff;
    --card-grey: #e3e5e8;
    --ink: #1c1c1c;
    --page-bg: #d9dbde;
  }
  * { box-sizing: border-box; margin: 0; padding: 0; }
  html, body {
    width: 1200px; height: 900px; overflow: hidden;
    background: var(--page-bg);
    font-family: "Arimo", Arial, sans-serif;
  }
  .canvas {
    width: 1200px; height: 900px;
    display: flex; flex-direction: column;
    align-items: center; justify-content: center; gap: 40px;
  }
  .card {
    position: relative;
    width: 700px; height: 392px;
    overflow: hidden;
    box-shadow: 0 6px 18px rgba(0,0,0,0.18);
  }
  .card__art { position: absolute; inset: 0; width: 100%; height: 100%; }

  .brand {
    position: absolute;
    display: flex; align-items: center; gap: 10px;
    color: var(--brand-blue);
    font-weight: 700;
    line-height: 1.05;
    text-transform: uppercase;
  }
  .brand__dot {
    flex: none;
    width: 16px; height: 16px; border-radius: 50%;
    background: var(--brand-blue);
  }

  /* Back card */
  .card--back .brand { left: 40px; top: 160px; width: 270px; font-size: 24px; }
  .services {
    position: absolute; left: 385px; top: 62px; width: 290px;
    color: var(--card-white);
    font-weight: 700;
  }
  .services__heading { font-size: 19px; margin-bottom: 4px; }
  .services__list { font-size: 14px; line-height: 1.3; margin-bottom: 18px; }
  .services__extra { font-size: 14px; }

  /* Front card */
  .card--front .brand { left: 62px; top: 78px; width: 440px; font-size: 32px; }
  .contacts {
    position: absolute; left: 62px; top: 228px;
    list-style: none;
    color: var(--ink);
  }
  .contacts__item {
    display: flex; align-items: center; gap: 14px;
    font-size: 18px; height: 30px;
  }
  .contacts__item--phone { font-size: 24px; font-weight: 700; }
  .contacts__icon { width: 18px; height: 18px; flex: none; fill: var(--brand-blue); }
</style>
</head>
<body>
<main class="canvas">

  <section class="card card--back" aria-label="Business card, services side">
    <svg class="card__art" viewBox="0 0 700 392" aria-hidden="true">
      <defs>
        <radialGradient id="backPaper" cx="0.3" cy="0.55" r="0.7">
          <stop offset="0" stop-color="#ffffff"/>
          <stop offset="1" stop-color="#dcdfe3"/>
        </radialGradient>
      </defs>
      <rect width="700" height="392" fill="var(--brand-blue)"/>
      <circle cx="30" cy="250" r="320" fill="url(#backPaper)"/>
    </svg>
    <div class="brand"><span class="brand__dot"></span><span>Brightway Haul &amp; Repair Services</span></div>
    <div class="services">
      <h2 class="services__heading">CLEAN</h2>
      <p class="services__list">Windows, Gutters, Solar Panels,<br>Driveways / Paths, Carpets.</p>
      <h2 class="services__heading">MOVE</h2>
      <p class="services__list">Small/Medium Size House/Office<br>Moves, Large Item pick-up &amp;<br>Delivery, Yard clean-up and removal</p>
      <p class="services__extra">General Maintenance &amp; Repairs</p>
    </div>
  </section>

  <section class="card card--front" aria-label="Business card, contact side">
    <svg class="card__art" viewBox="0 0 700 392" aria-hidden="true">
      <defs>
        <linearGradient id="frontPaper" x1="0" y1="0" x2="1" y2="1">
          <stop offset="0" stop-color="#ffffff"/>
          <stop offset="0.6" stop-color="#eef0f2"/>
          <stop offset="1" stop-color="#dfe2e6"/>
        </linearGradient>
      </defs>
      <rect width="700" height="392" fill="url(#frontPaper)"/>
      <rect y="350" width="700" height="8" fill="var(--brand-blue-light)"/>
      <rect y="358" width="700" height="34" fill="var(--brand-blue-dark)"/>
    </svg>
    <div class="brand"><span class="brand__dot"></span><span>Brightway Haul &amp; Repair Services</span></div>
    <ul class="contacts">
      <li class="contacts__item contacts__item--phone">
        <svg class="contacts__icon" viewBox="0 0 24 24" aria-hidden="true"><path d="M6.6 10.8a15 15 0 0 0 6.6 6.6l2.2-2.2c.3-.3.7-.4 1-.2 1.1.4 2.3.6 3.6.6.6 0 1 .4 1 1V20c0 .6-.4 1-1 1A17 17 0 0 1 3 4c0-.6.4-1 1-1h3.5c.6 0 1 .4 1 1 0 1.3.2 2.5.6 3.6.1.3 0 .7-.2 1z"/></svg>
        <span>0419574302</span>
      </li>
      <li class="contacts__item">
        <svg class="contacts__icon" viewBox="0 0 24 24" aria-hidden="true"><path d="M12 2a10 10 0 1 0 0 20 10 10 0 0 0 0-20zm6.9 6h-3a15 15 0 0 0-1.3-3.9A8 8 0 0 1 18.9 8zM12 4c.8 1.2 1.5 2.5 1.9 4h-3.8c.4-1.5 1.1-2.8 1.9-4zM4.3 14a8 8 0 0 1 0-4h3.4a16 16 0 0 0 0 4zm.8 2h3a15 15 0 0 0 1.3 3.9A8 8 0 0 1 5.1 16zm3-8h-3a8 8 0 0 1 4.3-3.9C8.8 5.3 8.4 6.6 8.1 8zM12 20c-.8-1.2-1.5-2.5-1.9-4h3.8c-.4 1.5-1.1 2.8-1.9 4zm2.3-6H9.7a14 14 0 0 1 0-4h4.6a14 14 0 0 1 0 4zm.3 5.9c.6-1.2 1-2.5 1.3-3.9h3a8 8 0 0 1-4.3 3.9zm1.7-5.9a16 16 0 0 0 0-4h3.4a8 8 0 0 1 0 4z"/></svg>
        <span>www.brightwayhaul.com.au</span>
      </li>
      <li class="contacts__item">
        <svg class="contacts__icon" viewBox="0 0 24 24" aria-hidden="true"><path d="M2 5h20v14H2zm2 2v.5l8 5 8-5V7zm0 2.8V17h16V9.8l-8 5z"/></svg>
        <span>brightwayhaulrepair@mailbox.example</span>
      </li>
    </ul>
  </section>

</main>
</body>
</html>
```